" Eu ( geriatra) vou ampliar meu Consultorio para uma empresa especializada no atendimento integral, personalizado e multiprofissional ao idoso. A ideia é oferecer pacotes com maior ou menor grau de atendimentos multiprofissionais "

```html
<!DOCTYPE html>
<html lang="pt-BR">
<head>
<meta charset="utf-8">
<title>Alvena – Crachás</title>
<link rel="stylesheet" href="https://fonts.googleapis.com/css2?family=Arimo:wght@400;700&display=swap">
<style>
  :root {
    --bg: #e9e9ea;
    --card: #ffffff;
    --ink: #222222;
    --muted: #7a7a7a;
    --brand: #8c8c8c;
    --bronze: #8a6a3f;
    --bronze-light: #b89a6c;
    --sand: #e6e0d8;
    --sand-deep: #d9d1c6;
    --line: #3a3a3a;
  }
  * { box-sizing: border-box; margin: 0; padding: 0; }
  html, body { width: 1200px; height: 1200px; overflow: hidden; }
  body {
    background: var(--bg);
    font-family: "Arimo", Arial, sans-serif;
    color: var(--ink);
    display: flex;
    align-items: center;
    justify-content: center;
    gap: 60px;
  }
  .badge {
    position: relative;
    width: 420px;
    height: 680px;
    background: var(--card);
    border-radius: 18px;
    overflow: hidden;
    box-shadow: 0 6px 22px rgba(0,0,0,0.12);
  }
  .badge__slot {
    position: absolute;
    top: 26px; left: 50%;
    width: 96px; height: 14px;
    margin-left: -48px;
    border-radius: 7px;
    background: var(--bg);
  }
  .brand {
    position: absolute;
    top: 95px; left: 0; right: 0;
    text-align: center;
  }
  .brand__mark {
    display: block;
    width: 28px; height: 28px;
    margin: 0 auto 10px;
    border-radius: 50%;
    background: var(--bronze-light);
  }
  .brand__name {
    font-size: 54px;
    font-weight: 400;
    color: var(--brand);
    letter-spacing: 1px;
    line-height: 1;
  }
  .brand__tagline {
    margin-top: 6px;
    font-size: 12px;
    letter-spacing: 2px;
    color: var(--bronze);
  }

  /* Front */
  .front__panel {
    position: absolute;
    left: 0; right: 0; top: 270px; bottom: 0;
    background: linear-gradient(180deg, var(--sand) 0%, #efebe5 60%, #f6f4f1 100%);
  }
  .front__photo {
    position: absolute;
    top: 300px; left: 50%;
    width: 150px; height: 200px;
    margin-left: -75px;
    background: var(--card);
    border: 5px solid var(--bronze);
    border-radius: 6px;
  }
  .front__holder {
    position: absolute;
    top: 530px; left: 0; right: 0;
    text-align: center;
  }
  .front__name {
    font-size: 30px;
    font-weight: 700;
    color: var(--bronze);
  }
  .front__role {
    margin-top: 6px;
    font-size: 22px;
    color: var(--muted);
  }
  .badge__rule {
    position: absolute;
    left: 0; right: 0; bottom: 46px;
    height: 5px;
    background: linear-gradient(90deg, var(--bronze-light), var(--bronze), var(--bronze-light));
  }

  /* Back */
  .back__fields {
    position: absolute;
    top: 285px; left: 36px; right: 36px;
  }
  .field {
    height: 52px;
    border: 2px solid var(--line);
    border-radius: 8px;
    padding: 6px 12px;
    font-size: 17px;
    margin-bottom: 34px;
  }
  .back__site {
    position: absolute;
    top: 495px; left: 0; right: 0;
    text-align: center;
    font-size: 17px;
    font-weight: 700;
  }
  .back__note {
    position: absolute;
    top: 545px; left: 34px; right: 34px;
    text-align: center;
    font-size: 16px;
    line-height: 1.35;
  }
  .back .badge__rule { background: var(--bronze); bottom: 42px; height: 7px; }
</style>
</head>
<body>
  <section class="badge front" aria-label="Crachá – frente">
    <div class="front__panel" role="img" aria-label="Fundo areia com motivo decorativo suave"></div>
    <span class="badge__slot"></span>
    <div class="brand">
      <span class="brand__mark"></span>
      <div class="brand__name">Alvena</div>
      <div class="brand__tagline">Saúde Geriátrica</div>
    </div>
    <div class="front__photo" role="img" aria-label="Espaço para foto do funcionário"></div>
    <div class="front__holder">
      <div class="front__name">Nome e Sobrenome</div>
      <div class="front__role">Cargo</div>
    </div>
    <div class="badge__rule"></div>
  </section>

  <section class="badge back" aria-label="Crachá – verso">
    <span class="badge__slot"></span>
    <div class="brand">
      <span class="brand__mark"></span>
      <div class="brand__name">Alvena</div>
      <div class="brand__tagline">Saúde Geriátrica</div>
    </div>
    <div class="back__fields">
      <div class="field">Nome Completo</div>
      <div class="field">Número Conselho</div>
    </div>
    <p class="back__site">www.alvenasaudegeriatrica.com.br</p>
    <p class="back__note">Esta identificação é de uso pessoal e intransferível, o funcionário deverá usar obrigatoriamente em horário comercial.</p>
    <div class="badge__rule"></div>
  </section>
</body>
</html>
```